Business Card

We need some ideas for corporate business cards. I'm interested in a double sided card, with one side featuring our corporate logo, the other side with employee information.

Corporate colors, logo etc. available at www.varnik.com

Industry/Entity Type

Business

Requirements
Must have
• The "Varnik" logo with stylized "O"

Nice to have
• Preferred font is calibri

```html
<!DOCTYPE html>
<html lang="en">
<head>
<meta charset="utf-8">
<title>Varnik Business Card</title>
<link rel="stylesheet" href="https://fonts.googleapis.com/css2?family=Open+Sans:wght@300;400;700&display=swap">
<style>
  :root {
    --ink: #201f20;
    --sky: #54a0d5;
    --paper: #ffffff;
    --stage: #c9ced4;
  }
  * { box-sizing: border-box; margin: 0; padding: 0; }
  html, body { width: 1200px; height: 900px; overflow: hidden; }
  body {
    background: var(--stage);
    font-family: "Open Sans", Calibri, sans-serif;
    position: relative;
  }
  .card {
    position: absolute;
    left: 250px;
    width: 700px;
    height: 400px;
    overflow: hidden;
    box-shadow: 0 8px 24px rgba(0,0,0,0.18);
  }
  .card--front { top: 40px; }
  .card--back { top: 470px; }
  .card__shapes { position: absolute; inset: 0; }
  .brand-name {
    position: absolute;
    left: 0; right: 0; top: 128px;
    text-align: center;
    color: var(--paper);
    font-weight: 400;
    font-size: 76px;
    letter-spacing: 10px;
  }
  .contact-list {
    position: absolute;
    right: 48px; top: 26px;
    list-style: none;
    color: var(--paper);
    font-weight: 300;
    font-size: 17px;
  }
  .contact-list li {
    display: flex;
    align-items: center;
    gap: 12px;
    height: 28px;
  }
  .contact-list svg { width: 20px; height: 20px; flex: none; }
  .person {
    position: absolute;
    left: 150px; top: 205px;
    color: var(--paper);
  }
  .person__name {
    font-weight: 700;
    font-size: 46px;
    line-height: 1;
    letter-spacing: 1px;
  }
  .person__role {
    font-weight: 300;
    font-size: 24px;
    margin-top: 6px;
    letter-spacing: 1px;
  }
</style>
</head>
<body>

<section class="card card--front" aria-label="Card front">
  <svg class="card__shapes" viewBox="0 0 700 400" aria-hidden="true">
    <rect width="700" height="400" fill="var(--ink)"/>
    <rect x="0" y="310" width="700" height="90" fill="var(--sky)"/>
    <rect x="380" y="270" width="200" height="90" rx="20" fill="var(--ink)"/>
    <rect x="-20" y="0" width="70" height="150" rx="20" fill="var(--sky)"/>
  </svg>
  <div class="brand-name">VARNIK</div>
</section>

<section class="card card--back" aria-label="Card back">
  <svg class="card__shapes" viewBox="0 0 700 400" aria-hidden="true">
    <rect width="700" height="400" fill="var(--sky)"/>
    <rect x="0" y="175" width="660" height="225" fill="var(--ink)"/>
    <rect x="200" y="140" width="240" height="80" rx="18" fill="var(--ink)"/>
    <rect x="60" y="345" width="190" height="90" rx="20" fill="var(--sky)"/>
  </svg>

  <ul class="contact-list">
    <li>
      <svg viewBox="0 0 20 20" aria-hidden="true"><path d="M10 2a6 6 0 0 0-6 6c0 4.5 6 10 6 10s6-5.5 6-10a6 6 0 0 0-6-6z" fill="none" stroke="#fff" stroke-width="1.8"/><circle cx="10" cy="8" r="2.2" fill="#fff"/></svg>
      123, Street name, Country
    </li>
    <li>
      <svg viewBox="0 0 20 20" aria-hidden="true"><path d="M5 2l3 4-2 2c1 2.5 3.5 5 6 6l2-2 4 3-2 3C9 17 3 11 2 4z" fill="#fff"/></svg>
      +852 555 0142
    </li>
    <li>
      <svg viewBox="0 0 20 20" aria-hidden="true"><rect x="2" y="4" width="16" height="12" fill="none" stroke="#fff" stroke-width="1.8"/><path d="M2 4l8 7 8-7" fill="none" stroke="#fff" stroke-width="1.6"/></svg>
      email@varnik.com
    </li>
    <li>
      <svg viewBox="0 0 20 20" aria-hidden="true"><circle cx="10" cy="10" r="8" fill="none" stroke="#fff" stroke-width="1.8"/><path d="M2 10h16M10 2c3 3 3 13 0 16M10 2c-3 3-3 13 0 16" fill="none" stroke="#fff" stroke-width="1.2"/></svg>
      www.varnik.com
    </li>
  </ul>

  <div class="person">
    <div class="person__name">NAME HERE</div>
    <div class="person__role">POSITION/CEO</div>
  </div>
</section>

</body>
</html>
```